QM Interiors needs and Interior Design Business card

I can do anything from Commercial to Residential and Free lance. Beginning to end in design selection process.
Need something to catch the eye of potential customers and vendors. From furniture to Tile and Cabinet selections. I can do it all.

Industry/Entity Type

Design Agency

Contact Information for Business Card

QM Interiors- Design Consultanting Residential, Commerical
Maybe a cool detail background. Wall paper print that can have some texture

Font styles to use
Serif

Colors
709dcb
34a6d7
b868aa
e667a6
f59296
85acd3
ffffff
000000
5c5c5c

Requirements
Must have
• Square or Rectangular with Rounded edges
• Name
• Address
• Phone
• Email
Nice to have
• Some colored edges More simples not too busy
• Pattern detail in background.
Should not have
• Not too much color

```html
<!DOCTYPE html>
<html lang="en">
<head>
<meta charset="utf-8">
<title>QM Interiors – Business Card</title>
<link rel="stylesheet" href="https://fonts.googleapis.com/css2?family=Source+Sans+3:wght@400;600&display=swap">
<style>
  :root {
    --stage-top: #2b2b2b;
    --stage-bottom: #040404;
    --card-blue: #35a6d8;
    --ink-dark: #1e1b1c;
    --band-dark: #231f20;
    --paper-white: #ffffff;
  }
  * { margin: 0; padding: 0; box-sizing: border-box; }
  html, body { width: 1200px; height: 900px; overflow: hidden; }
  body {
    position: relative;
    background: linear-gradient(180deg, var(--stage-top) 0%, #161616 45%, var(--stage-bottom) 100%);
    font-family: "Source Sans 3", "Myriad Pro", Arial, sans-serif;
  }
  .card {
    position: absolute;
    top: 306px;
    width: 439px;
    height: 271px;
    background: var(--card-blue);
    border-radius: 11px;
    overflow: hidden;
  }
  .card--front { left: 149px; }
  .card--back { left: 608px; }

  .side-band {
    position: absolute;
    left: 61px; top: 0;
    width: 55px; height: 100%;
    background: var(--band-dark);
  }
  .badge {
    position: absolute;
    left: 24px; top: 68px;
    width: 128px; height: 128px;
    border-radius: 50%;
    background: var(--card-blue);
    border: 5px solid var(--band-dark);
    display: flex; align-items: center; justify-content: center;
  }
  .badge__name {
    font-size: 14px; font-weight: 600;
    color: var(--ink-dark);
  }
  .person { position: absolute; left: 139px; top: 28px; color: var(--paper-white); }
  .person__name { font-size: 18.5px; font-weight: 600; line-height: 1.1; }
  .person__title { font-size: 14px; font-weight: 400; margin-top: 1px; }

  .address {
    position: absolute; left: 159px; top: 120px;
    font-size: 12.5px; line-height: 15px; color: var(--ink-dark);
  }
  .contact {
    position: absolute; left: 140px; top: 208px;
    list-style: none; color: var(--paper-white);
    font-size: 14px; line-height: 18px;
  }
  .contact li { display: flex; align-items: center; gap: 7px; }
  .contact svg { width: 10px; height: 10px; fill: var(--paper-white); }

  .brand {
    position: absolute; left: 0; top: 52px; width: 100%;
    display: flex; flex-direction: column; align-items: center;
    color: var(--ink-dark);
  }
  .brand__circle {
    width: 96px; height: 96px; border-radius: 50%;
    border: 4px solid var(--ink-dark);
  }
  .brand__name {
    margin-top: 8px;
    font-size: 29px; font-weight: 400; letter-spacing: 4px;
  }
  .brand__tagline { margin-top: 12px; font-size: 12.5px; }
</style>
</head>
<body>
  <section class="card card--front">
    <div class="side-band"></div>
    <div class="badge"><span class="badge__name">QM Interiors</span></div>
    <div class="person">
      <p class="person__name">Daniel Hart</p>
      <p class="person__title">Managing Director</p>
    </div>
    <p class="address">12345, Address Goes Here<br>Country Name, 123456.</p>
    <ul class="contact">
      <li><svg viewBox="0 0 10 10"><path d="M2 0.5 L3.6 2.6 L2.7 3.6 C3.3 5 4.8 6.6 6.3 7.3 L7.3 6.3 L9.5 8 L8.4 9.5 C4.5 9.2 0.8 5.5 0.5 1.6 Z"/></svg>055-987 654 321</li>
      <li><svg viewBox="0 0 10 10"><path d="M0.5 2 H9.5 V8.5 H0.5 Z M1 2.5 L5 5.5 L9 2.5" fill="var(--paper-white)" stroke="var(--card-blue)" stroke-width="0.8"/></svg>hello@qmstudio.com</li>
    </ul>
  </section>

  <section class="card card--back">
    <div class="brand">
      <div class="brand__circle"></div>
      <p class="brand__name">QM Interiors</p>
      <p class="brand__tagline">Design Consultanting Residential, Commerical</p>
    </div>
  </section>
</body>
</html>
```